PROFESSIONAL MODERN REDESIGN OF CURRENT WEBSITE USING ALL SAME CONTENT

I need to redesign existing website using all existing exact content. Please do not leave anything missing. Use all content.

www.brightpathpromotionsgroup.biz

Target Market(s)

Small business owners, business to business, B2B

Industry/Entity Type

Direct Marketing

Number of Pages Required

5+ page

Colors

Designer to choose colors to be used in the design.

Requirements
Must have
• Must use exact same content as www.brightpathpromotionsgroup.biz
Nice to have
• I'd like this to be an easy to read professionally designed website with all modern elements...
Should not have
• Open

```html
<!DOCTYPE html>
<html lang="en">
<head>
<meta charset="utf-8">
<title>Bright Path Promotions – Samples</title>
<link href="https://fonts.googleapis.com/css2?family=Lexend+Zetta:wght@800&family=Poppins:wght@400;500;600;700&display=swap" rel="stylesheet">
<style>
:root{
  --blue:#1577c4;
  --blue-dark:#0f64a8;
  --green:#4caf50;
  --ink:#111;
  --text:#333;
  --muted:#888;
  --panel:#ececec;
  --footer:#12222e;
  --footer-line:#2a3b48;
  --grey-btn:#5b6470;
}
*{box-sizing:border-box;margin:0;padding:0}
html,body{width:1121px;height:1200px;overflow:hidden}
body{font-family:"Poppins",sans-serif;color:var(--text);background:#fff;position:relative}
.display{font-family:"Lexend Zetta",sans-serif;font-weight:800;letter-spacing:-1.5px;text-transform:uppercase}

/* header */
.site-header{position:absolute;top:0;left:0;width:1121px;height:57px;display:flex;background:var(--blue)}
.brand{width:336px;height:57px;background:#fff;clip-path:polygon(0 0,100% 0,94% 100%,0 100%);display:flex;align-items:center;padding-left:30px;gap:8px}
.brand-mark{width:22px;height:22px;background:var(--blue);border-radius:50%}
.brand-name{font-weight:700;font-size:14px;color:var(--blue);line-height:1.1}
.main-nav{display:flex;align-items:center;flex:1;padding-left:22px}
.main-nav a{color:#fff;text-decoration:none;font-size:10.5px;font-weight:500;padding:0 7px;border-right:1px solid rgba(255,255,255,.25)}
.main-nav a:last-child{border:none}
.main-nav a.active{font-weight:700}
.hdr-btn{width:65px;height:57px;display:flex;flex-direction:column;align-items:center;justify-content:center;color:#fff;font-size:9.5px;font-weight:500;gap:4px}
.hdr-btn.login{background:var(--grey-btn)}
.hdr-btn.signup{background:var(--blue-dark)}
.hdr-phone{width:169px;height:57px;background:var(--green);display:flex;align-items:center;gap:8px;padding-left:18px;color:#fff}
.hdr-phone small{display:block;font-size:8.5px}
.hdr-phone strong{font-size:14px;font-weight:700}

/* hero */
.hero{position:absolute;top:57px;left:0;width:1121px;height:256px;background:linear-gradient(120deg,#5d5b57,#4a4845 40%,#3f3c38 70%,#6a6150);display:flex;align-items:center;justify-content:center}
.hero h1{color:#fff;font-size:26px;text-align:center;line-height:1.35}

/* samples */
.samples{position:absolute;top:385px;left:0;width:1121px;text-align:center}
.samples h2{font-size:22px;color:var(--ink)}
.samples h2 span{color:var(--blue)}
.samples .lead{margin-top:10px;font-size:12px;line-height:1.5;color:#333}
.form-card{position:absolute;top:485px;left:221px;width:680px;height:266px;background:#fff;box-shadow:0 0 14px rgba(0,0,0,.08);padding:6px}
.form-panel{background:var(--panel);height:254px;padding:28px 19px 0;display:grid;grid-template-columns:300px 300px;column-gap:28px;row-gap:0}
.field label{display:block;font-size:10.5px;font-weight:500;color:var(--blue);margin:0 0 8px 4px;text-transform:uppercase}
.field .input{height:42px;background:#fff;border-radius:2px;display:flex;align-items:center;justify-content:space-between;padding:0 16px;font-size:9.5px;color:#777;margin-bottom:32px}
.field .caret{width:0;height:0;border-left:4px solid transparent;border-right:4px solid transparent;border-top:5px solid var(--blue)}
.download-btn{position:absolute;top:721px;left:378px;width:365px;height:53px;background:var(--green);border-radius:3px;display:flex;align-items:center;justify-content:center;gap:12px;color:#fff;font-size:13px}
.note{position:absolute;top:787px;left:0;width:1121px;text-align:center;font-size:9.5px}
.note b{color:var(--blue);font-weight:500}

/* footer */
.site-footer{position:absolute;top:866px;left:0;width:1121px;height:334px;background:var(--footer);color:#cfd6dc}
.f-col{position:absolute;top:52px}
.f-col h3{color:#fff;font-size:12px;margin-bottom:14px}
.f-brand{left:120px;width:210px;text-align:center;top:60px}
.f-brand .name{font-weight:700;color:var(--blue);font-size:16px;display:flex;align-items:center;justify-content:center;gap:8px}
.f-brand .name i{width:16px;height:16px;border-radius:50%;background:var(--blue)}
.socials{display:flex;justify-content:center;gap:8px;margin-top:22px}
.socials span{width:30px;height:30px;border-radius:50%;background:#8a8f94}
.free-pack{margin:21px auto 0;width:194px;height:42px;background:var(--green);color:#fff;display:flex;flex-direction:column;align-items:center;justify-content:center}
.free-pack b{font-size:11px}
.free-pack small{font-size:8px}
.divider{position:absolute;top:48px;width:1px;height:175px;background:var(--footer-line)}
.contact{left:369px;width:270px}
.contact p{font-size:10px;line-height:1.6;margin-bottom:10px;padding-left:19px;position:relative}
.contact p svg{position:absolute;left:0;top:3px}
.contact strong{color:#fff}
.contact .closed{color:var(--green);font-weight:500}
.links{font-size:10px}
.links ul{list-style:none}
.links li{margin-bottom:7px}
.quick{left:662px}
.quick ul{padding-left:4px}
.others{left:817px}
.f-bottom{position:absolute;top:291px;left:122px;width:878px;border-top:1px solid var(--footer-line);padding-top:12px;display:flex;justify-content:space-between;font-size:10px;color:#9aa4ac}
.f-bottom strong{color:#fff}
</style>
</head>
<body>

<header class="site-header">
  <div class="brand"><span class="brand-mark"></span><span class="brand-name">Bright Path Promotions</span></div>
  <nav class="main-nav">
    <a class="active">Home</a><a>Our Incentives</a><a>Samples</a><a>Affiliates</a><a>Testimonials</a><a>Faq</a><a>Contact Us</a>
  </nav>
  <div class="hdr-btn login">
    <svg width="13" height="13" viewBox="0 0 12 12"><circle cx="6" cy="3.5" r="2.7" fill="#fff"/><path d="M1 12a5 4 0 0 1 10 0z" fill="#fff"/></svg>LOGIN
  </div>
  <div class="hdr-btn signup">
    <svg width="13" height="13" viewBox="0 0 12 12"><circle cx="6" cy="6" r="5.2" fill="none" stroke="#fff"/><path d="M6 9V3.5M3.8 5.6 6 3.4l2.2 2.2" stroke="#fff" fill="none"/></svg>SIGN UP
  </div>
  <div class="hdr-phone">
    <svg width="14" height="26" viewBox="0 0 14 26"><rect x="1" y="1" width="12" height="24" rx="2" fill="none" stroke="#fff" stroke-width="2"/><circle cx="7" cy="21" r="1.3" fill="#fff"/></svg>
    <div><small>USA Office :</small><strong>555-214-3080</strong></div>
  </div>
</header>

<section class="hero" role="img" aria-label="Muted photo of a person sketching marketing plans at a desk">
  <h1 class="display">Test out our easy online<br>redemption process now!</h1>
</section>

<section class="samples">
  <h2 class="display">Download free <span>samples below</span></h2>
  <p class="lead">Enter Your Details. We Will Send You A Digital E Certificate By Email, An Sms Certificate By Text And You<br>Will Be Able To Instantly Download A Pdf Sample.</p>
</section>

<div class="form-card">
  <div class="form-panel">
    <div class="field"><label>Select Certificate To Redeem *</label><div class="input">Select A Certificate From The List... <span class="caret"></span></div></div>
    <div class="field"><label>Full Name*</label><div class="input">Enter Your Name</div></div>
    <div class="field"><label>Email*</label><div class="input">Enter Your Email Address...</div></div>
    <div class="field"><label>Phone*</label><div class="input">123-456-7890</div></div>
  </div>
</div>

<div class="download-btn display">
  <svg width="28" height="32" viewBox="0 0 28 32"><path d="M4 1h14l7 7v23H4z" fill="none" stroke="#fff" stroke-width="2"/><rect x="1" y="14" width="20" height="9" fill="#fff"/><text x="11" y="21" font-size="6" text-anchor="middle" fill="#4caf50" font-family="Poppins,sans-serif">PDF</text></svg>
  Download pdf certificate
</div>
<p class="note"><b>Note</b>: Turn Off Your Pop Up Blocker To View The Pdf Samples</p>

<footer class="site-footer">
  <div class="f-col f-brand">
    <div class="name"><i></i>Bright Path Promotions</div>
    <div class="socials"><span></span><span></span><span></span><span></span></div>
    <div class="free-pack"><b class="display">Get a 100% free</b><small>SAMPLE PACKAGE</small></div>
  </div>
  <div class="divider" style="left:348px"></div>
  <div class="f-col contact">
    <h3 class="display">Contact us</h3>
    <p><svg width="11" height="13" viewBox="0 0 11 13"><path d="M5.5 12S1 7.5 1 5a4.5 4.5 0 0 1 9 0c0 2.5-4.5 7-4.5 7z" fill="none" stroke="#9aa4ac"/><circle cx="5.5" cy="5" r="1.5" fill="none" stroke="#9aa4ac"/></svg><strong>Bright Path Promotions Group, Inc.</strong><br>1450 Harbor View Lane Portside CA 90000</p>
    <p><svg width="12" height="12" viewBox="0 0 12 12"><path d="M2 1l2 2-1 1.5a7 7 0 0 0 4.5 4.5L9 8l2 2-1.5 1.5C5 11 1 7 .5 2.5z" fill="none" stroke="#9aa4ac"/></svg>USA Office : <strong>555-214-3080</strong><br>International : <strong>1-800-555-0147</strong></p>
    <p><svg width="12" height="10" viewBox="0 0 12 10"><rect x=".5" y=".5" width="11" height="9" fill="none" stroke="#9aa4ac"/><path d="M.5.5 6 5.5 11.5.5" fill="none" stroke="#9aa4ac"/></svg>hello@brightpathpromotionsgroup.biz</p>
    <p><svg width="12" height="12" viewBox="0 0 12 12"><circle cx="6" cy="6" r="5.5" fill="none" stroke="#9aa4ac"/><path d="M6 3v3l2 1.5" fill="none" stroke="#9aa4ac"/></svg>Hours : Mon-fri 08am - 05pm Pst<br><span class="closed">SAT-SUN CLOSED</span></p>
  </div>
  <div class="divider" style="left:641px"></div>
  <div class="f-col links quick">
    <h3 class="display">Quick links</h3>
    <ul><li>Home</li><li>Our Incetives</li><li>Samples</li><li>Affiliate</li><li>Testimonials</li><li>Faq</li><li>Contact Us</li></ul>
  </div>
  <div class="divider" style="left:796px"></div>
  <div class="f-col links others">
    <h3 class="display">Others links</h3>
    <ul><li>Hoteliers</li><li>Bpp Pdf Flyer</li><li>Bpp Pdf Brochure</li><li>Bpp Certificates List</li><li>How To Use Bpp Certificates</li><li>Free Video Ad Mock Up For Marketing</li></ul>
  </div>
  <div class="f-bottom">
    <span>© 2020 <strong>Bright Path Promotions.</strong> All Rights Reserved.</span>
    <span>Privacy Policy &nbsp;I&nbsp; Term And Conditions</span>
  </div>
</footer>

</body>
</html>
```